Fernquill Stationary Design
The Ledger Desk Firm
Fernquill Stationary Design -
Creative Brief
Professional
Marla Dempton
3847 W. Harlan Pkwy. Suite 410 Irving, TX 75061
mdempton@fernquill.example
www.fernquill.example
We want to be different in our space. Most if not all of our competitors have boring, text-intensive websites. We want to be different. We're agile, nimple, quick, crisp, entrepreneurial, hip/cool.
Logo, Tagline (The Ledger Desk Firm) and our website address (www.fernquill.example) At the end of the day, play around with what looks cool!

```html
<!DOCTYPE html>
<html lang="en">
<head>
<meta charset="utf-8">
<title>Fernquill Stationery</title>
<link href="https://fonts.googleapis.com/css2?family=Open+Sans:wght@400;700;800&display=swap" rel="stylesheet">
<style>
:root{
  --green:#7dbb2b;
  --green-dark:#5e9a1a;
  --black:#1b1b1b;
  --ink:#444;
  --muted:#9a9a9a;
  --paper:#ffffff;
  --faint:#eeeeee;
  --shadow:0 2px 4px rgba(0,0,0,.25);
}
*{box-sizing:border-box;margin:0;padding:0}
html,body{width:1200px;height:310px;overflow:hidden;background:#fff;font-family:"Open Sans",Arial,sans-serif}
.canvas{position:relative;width:1200px;height:310px}
.piece{position:absolute;background:var(--paper);box-shadow:var(--shadow);overflow:hidden}
.brand{display:flex;align-items:center;gap:3px;font-weight:800;color:var(--black);letter-spacing:.3px}
.brand .dot{border-radius:50%;background:var(--green);flex:none}
.brand.light{color:#fff}
.card{width:125px;height:67px}
.card.dark{background:var(--black)}
.card.green{background:var(--green)}
.card .brand{font-size:8px}
.card .brand .dot{width:8px;height:8px}
.center{display:flex;align-items:center;justify-content:center}
.card-info{position:absolute;font-size:4px;line-height:1.5;color:var(--ink)}
.card-info.light{color:#ddd}
.card-info strong{font-size:5px;color:var(--green)}
.strip{position:absolute;left:0;right:0;bottom:0;height:12px;background:var(--green)}
.letter{width:197px;height:276px;top:12px}
.letter .brand{position:absolute;left:12px;top:12px;font-size:8px}
.letter .brand .dot{width:8px;height:8px}
.letter .contact{position:absolute;right:12px;top:10px;font-size:3.5px;line-height:1.5;color:var(--muted);text-align:right}
.letter .mark{position:absolute;left:50%;top:48px;width:118px;height:118px;margin-left:-59px;border-radius:50%;background:var(--faint)}
.letter .foot{position:absolute;left:0;right:0;bottom:8px;text-align:center;font-size:3.5px;color:var(--muted)}
.env{width:225px}
.env .brand{position:absolute;left:10px;top:10px;font-size:8px}
.env .brand .dot{width:8px;height:8px}
.env .addr{position:absolute;left:10px;top:22px;font-size:3.5px;line-height:1.5;color:var(--muted)}
.env .band{position:absolute;left:0;right:0;bottom:0;background:var(--green)}
.env .site{position:absolute;right:10px;bottom:3px;font-size:4px;color:#fff}
.flap{position:absolute;left:940px;width:253px}
</style>
</head>
<body>
<main class="canvas">

  <!-- business cards -->
  <section class="piece card dark center" style="left:7px;top:36px"><div class="brand light"><span class="dot"></span>FERNQUILL</div></section>
  <section class="piece card dark" style="left:144px;top:36px">
    <div class="brand light" style="position:absolute;left:8px;top:7px;font-size:6px"><span class="dot" style="width:6px;height:6px"></span>FERNQUILL</div>
    <div class="card-info light" style="left:8px;top:24px"><strong>Marla Dempton</strong><br>Managing Director<br>P 214.555.0142<br>mdempton@fernquill.example<br>www.fernquill.example</div>
  </section>

  <section class="piece card center" style="left:7px;top:120px"><div class="brand"><span class="dot"></span>FERNQUILL</div><div class="strip" style="height:6px"></div></section>
  <section class="piece card" style="left:144px;top:120px">
    <div class="card-info" style="left:8px;top:8px"><strong>Marla Dempton</strong><br>Managing Director</div>
    <div class="card-info" style="left:8px;top:32px">3847 W. Harlan Pkwy. Suite 410<br>Irving, TX 75061<br>P 214.555.0142<br>mdempton@fernquill.example</div>
    <div class="brand" style="position:absolute;right:6px;top:8px;font-size:5px"><span class="dot" style="width:5px;height:5px"></span>FERNQUILL</div>
  </section>

  <section class="piece card" style="left:7px;top:204px">
    <div class="card-info" style="left:8px;top:50px;color:var(--muted)">www.fernquill.example</div>
  </section>
  <section class="piece card green center" style="left:144px;top:204px"><div class="brand light"><span class="dot" style="background:#fff"></span>FERNQUILL</div></section>

  <!-- letterheads -->
  <section class="piece letter" style="left:271px">
    <div class="brand"><span class="dot"></span>FERNQUILL</div>
    <div class="contact">3847 W. Harlan Pkwy. Suite 410<br>Irving, TX 75061<br>P 214.555.0142</div>
    <div class="mark" role="img" aria-label="Faint brand circle"></div>
    <div class="foot">www.fernquill.example</div>
  </section>
  <section class="piece letter" style="left:487px">
    <div class="brand"><span class="dot"></span>FERNQUILL</div>
    <div class="contact">3847 W. Harlan Pkwy. Suite 410<br>Irving, TX 75061<br>P 214.555.0142</div>
    <div class="mark" role="img" aria-label="Faint brand circle"></div>
    <div class="foot">www.fernquill.example</div>
  </section>

  <!-- envelopes -->
  <section class="piece env" style="left:700px;top:115px;height:97px">
    <div class="brand"><span class="dot"></span>FERNQUILL</div>
    <div class="addr">3847 W. Harlan Pkwy. Suite 410<br>Irving, TX 75061</div>
    <div class="band" style="height:12px"><span class="site">www.fernquill.example</span></div>
  </section>
  <section class="piece env" style="left:700px;top:228px;height:58px">
    <div class="brand"><span class="dot"></span>FERNQUILL</div>
    <div class="band" style="height:10px"></div>
  </section>

  <!-- envelope backs -->
  <svg class="flap" style="top:58px" height="92" viewBox="0 0 253 92" aria-hidden="true">
    <defs><linearGradient id="darkFlap" x1="0" y1="0" x2="0" y2="1"><stop offset="0" stop-color="#555"/><stop offset="1" stop-color="#111"/></linearGradient></defs>
    <rect width="253" height="92" fill="url(#darkFlap)"/>
    <circle cx="126" cy="30" r="9" fill="var(--green)"/>
  </svg>
  <svg class="flap" style="top:140px;filter:drop-shadow(0 2px 3px rgba(0,0,0,.25))" height="82" viewBox="0 0 253 82" aria-hidden="true">
    <rect width="253" height="82" fill="#fff"/>
    <polygon points="0,0 253,0 253,8 126,46 0,8" fill="var(--green)"/>
  </svg>
  <svg class="flap" style="top:214px;filter:drop-shadow(0 2px 3px rgba(0,0,0,.25))" height="76" viewBox="0 0 253 76" aria-hidden="true">
    <rect width="253" height="76" fill="#fff"/>
    <polyline points="0,2 126,40 253,2" fill="none" stroke="#ccc" stroke-width="1"/>
    <polyline points="0,76 110,36" fill="none" stroke="#e2e2e2" stroke-width="1"/>
    <polyline points="253,76 142,36" fill="none" stroke="#e2e2e2" stroke-width="1"/>
  </svg>

</main>
</body>
</html>
```